Tellborne Medical

Need smart and sleek business cards design for my medical distribution company. use logos attached.

add my details

Lorcan Pettifer
Director/Sales Agent
lorcan@tellbornemedical-example.com.au
0491 638 170

```html
<!DOCTYPE html>
<html lang="en">
<head>
<meta charset="utf-8">
<title>Tellborne Medical – Business Cards</title>
<link rel="stylesheet" href="https://fonts.googleapis.com/css2?family=Lato:wght@400;700;900&display=swap">
<style>
  :root {
    --stage: #2b2b2b;
    --navy: #03225e;
    --sky: #2a86c4;
    --white: #ffffff;
    --paper: #ffffff;
    --rule: #2a6fae;
  }
  * { margin: 0; padding: 0; box-sizing: border-box; }
  html, body { width: 1200px; height: 875px; overflow: hidden; }
  body {
    background: var(--stage);
    font-family: "Lato", Arial, sans-serif;
    display: flex;
    flex-direction: column;
    align-items: center;
    justify-content: center;
    gap: 40px;
  }
  .card {
    width: 640px;
    height: 366px;
    border-radius: 22px;
    position: relative;
    overflow: hidden;
    box-shadow: 0 14px 30px rgba(0,0,0,.45);
  }

  /* Front */
  .card-front { background: var(--paper); display: flex; align-items: center; justify-content: center; }
  .wordmark { display: flex; align-items: center; gap: 14px; }
  .wordmark-square { width: 34px; height: 34px; background: var(--sky); }
  .wordmark-name {
    font-weight: 900;
    color: var(--navy);
    font-size: 46px;
    letter-spacing: 1px;
    text-transform: uppercase;
  }

  /* Back */
  .card-back { background: var(--navy); color: var(--white); }
  .back-logo {
    position: absolute; left: 40px; top: 50%; transform: translateY(-50%);
    display: flex; align-items: center; gap: 9px;
  }
  .back-logo .wordmark-square { width: 16px; height: 16px; }
  .back-logo .wordmark-name { color: var(--white); font-size: 20px; letter-spacing: .5px; }
  .divider {
    position: absolute; left: 300px; top: 100px; width: 1px; height: 150px;
    background: var(--rule);
  }
  .details { position: absolute; left: 330px; top: 104px; }
  .person-name {
    font-weight: 900; color: var(--sky); font-size: 24px;
    text-transform: uppercase; letter-spacing: .5px;
  }
  .person-role { font-size: 14px; margin: 4px 0 16px; }
  .contact-list { list-style: none; font-size: 12.5px; }
  .contact-list li { display: flex; align-items: center; gap: 9px; margin-bottom: 7px; }
  .contact-list svg { width: 11px; height: 11px; fill: var(--sky); flex: none; }
  .edge-band { position: absolute; left: 0; right: 0; bottom: 0; height: 12px; display: flex; align-items: flex-end; }
  .edge-white { flex: 0 0 66%; height: 5px; background: var(--white); }
  .edge-blue { flex: 1; height: 12px; background: var(--sky); }
</style>
</head>
<body>
  <section class="card card-front" aria-label="Card front">
    <div class="wordmark">
      <span class="wordmark-square"></span>
      <span class="wordmark-name">Tellborne Medical</span>
    </div>
  </section>

  <section class="card card-back" aria-label="Card back">
    <div class="back-logo">
      <span class="wordmark-square"></span>
      <span class="wordmark-name">Tellborne Medical</span>
    </div>
    <div class="divider"></div>
    <div class="details">
      <h1 class="person-name">Lorcan Pettifer</h1>
      <p class="person-role">Director / Sales Agent</p>
      <ul class="contact-list">
        <li>
          <svg viewBox="0 0 24 24" aria-hidden="true"><path d="M6.6 10.8a15 15 0 0 0 6.6 6.6l2.2-2.2a1 1 0 0 1 1-.25 11.4 11.4 0 0 0 3.6.57 1 1 0 0 1 1 1V20a1 1 0 0 1-1 1A17 17 0 0 1 3 4a1 1 0 0 1 1-1h3.5a1 1 0 0 1 1 1c0 1.25.2 2.45.57 3.57a1 1 0 0 1-.25 1z"/></svg>
          0491 638 170
        </li>
        <li>
          <svg viewBox="0 0 24 24" aria-hidden="true"><path d="M2 5h20v14H2z M2 5l10 8 10-8" /></svg>
          lorcan@tellbornemedical-example.com.au
        </li>
        <li>
          <svg viewBox="0 0 24 24" aria-hidden="true"><path d="M12 2a10 10 0 1 0 0 20 10 10 0 0 0 0-20zm0 2.2a7.8 7.8 0 1 1 0 15.6 7.8 7.8 0 0 1 0-15.6z"/></svg>
          tellbornemedical-example.com.au
        </li>
      </ul>
    </div>
    <div class="edge-band"><span class="edge-white"></span><span class="edge-blue"></span></div>
  </section>
</body>
</html>
```